Renew plant-based protein powder label

I would like a redesign for my current protein powder label . The current label idea should not be altered too much, but the design should be taken to the next level. Keep in mind that is should remain professional, not too extravagant. The main color for this label should remain red, because I represent each of my products with a specific color. It would be nice if a subtle (green) touch could be implemented to represent the plant based protein.

The logo should not be altered, and I prefer designs in Adobe Indesign (so I can adjust minor things if necessary later on).
Updates

Some adjustments to my project description: I generally like the idea of my current label but think that it can be uplifted even more. For instance, I like the idea of the hexagon structures as it is now, but it can be done better (try to create a 'wow-effect'). This does not mean that I exclude any other ideas, but they should be really good as otherwise it does not make any sense switching my entire product line to the new label format. The leaf picture that I included is not mandatory to use (as I have seen this a lot). I think the way in which Design #27872840 presented the bottom information (nr. of doses etc.) is creative. But as I mentioned, I intend to adjust the whole product line to this format so it has to be really good. Thanks a lot for your efforts and I look forward to new creativity.

Target Market(s)

Fitness market. usual customer is aged 18-25.

Industry/Entity Type

Fitness. Weight lifting.

Other font styles liked:
• See fonts attached that I use now. Use no script fonts.

Colors
00AB8E
00BBA5
67D7C9
C6EFE9
E9F9F6
EB3D1F
EC4F4E
F09395
F8D3D4
FCEDEE

Requirements
Must have
• The current design idea implemented.
Nice to have
• A subtle, but creative element of the plant-based aspect. Try to keep the main color red.
Should not have
• Extravagant designs

```html
<!DOCTYPE html>
<html lang="en">
<head>
<meta charset="UTF-8">
<title>Pure Cacao Plant Protein Label</title>
<link href="https://fonts.googleapis.com/css2?family=Nunito:ital,wght@1,900&family=Open+Sans:wght@400;700&display=swap" rel="stylesheet">
<style>
  :root {
    --page: #ffffff;
    --label-black: #05060b;
    --label-edge: #22232a;
    --brand-white: #ffffff;
    --brand-dot: #2a86cf;
    --cacao-red: #e3001b;
    --protein-blue: #2a8ed0;
    --leaf-green: #1fa64a;
    --servings-blue: #2a8fd0;
    --weight-pink: #c064a8;
    --hex-purple: #5a2a6e;
    --hex-blue: #1b63c9;
  }
  * { margin: 0; padding: 0; box-sizing: border-box; }
  html, body {
    width: 1200px; height: 1200px; overflow: hidden;
    background: var(--page);
  }
  .label {
    position: absolute; left: 165px; top: 40px;
    width: 870px; height: 1120px;
    background: linear-gradient(90deg, var(--label-edge) 0%, var(--label-black) 8%, var(--label-black) 92%, var(--label-edge) 100%);
    overflow: hidden;
  }
  .brand {
    position: absolute; left: 0; right: 0; top: 190px;
    display: flex; justify-content: center; align-items: center; gap: 18px;
    font-family: "Open Sans", sans-serif; font-weight: 400;
    color: var(--brand-white); text-align: left;
  }
  .brand-dot {
    width: 26px; height: 26px; border-radius: 50%;
    background: var(--brand-dot);
  }
  .brand-name { font-size: 46px; line-height: 1.05; letter-spacing: 3px; }
  .product-pill {
    position: absolute; left: 48px; top: 406px;
    width: 776px; height: 158px; border-radius: 60px;
    background: var(--cacao-red);
    display: flex; align-items: center; justify-content: center;
  }
  .product-name {
    font-family: "Nunito", sans-serif; font-style: italic; font-weight: 900;
    font-size: 108px; line-height: 1; letter-spacing: 1px;
    white-space: nowrap; color: var(--brand-white);
  }
  .protein-line {
    position: absolute; left: 0; right: 0; top: 618px;
    display: flex; justify-content: center; align-items: center; gap: 26px;
  }
  .leaf-icon {
    width: 50px; height: 90px;
    background: var(--leaf-green);
    border-radius: 50% 0 50% 0;
    transform: rotate(20deg);
  }
  .protein-text {
    font-family: "Open Sans", sans-serif; font-weight: 700;
    font-size: 84px; line-height: 1; color: var(--protein-blue); letter-spacing: -1px;
    white-space: nowrap;
  }
  .hex-field {
    position: absolute; left: 0; right: 0; top: 820px; bottom: 0;
    background: linear-gradient(180deg, rgba(5,6,11,0) 0%, var(--hex-purple) 40%, var(--hex-blue) 100%);
  }
  .servings-box {
    position: absolute; left: 257px; top: 788px;
    width: 362px; height: 96px;
    background: var(--servings-blue);
    display: flex; align-items: center; justify-content: center;
    font-family: "Open Sans", sans-serif; font-weight: 700;
    font-size: 52px; color: var(--brand-white); white-space: nowrap;
  }
  .weight-box {
    position: absolute; left: 296px; top: 1018px;
    width: 272px; height: 90px;
    background: var(--weight-pink);
    display: flex; align-items: center; justify-content: center;
    font-family: "Open Sans", sans-serif; font-weight: 700;
    font-size: 44px; color: var(--brand-white); white-space: nowrap;
  }
</style>
</head>
<body>
  <main class="label">
    <div class="brand">
      <span class="brand-dot"></span>
      <span class="brand-name">VERDA<br>NUTRITION</span>
    </div>

    <div class="product-pill">
      <h1 class="product-name">PURE CACAO</h1>
    </div>

    <div class="protein-line">
      <span class="leaf-icon" role="img" aria-label="Small green leaf icon"></span>
      <span class="protein-text">Plant Protein</span>
    </div>

    <div class="hex-field" role="img" aria-label="Glowing hexagon molecular pattern in purple and blue"></div>

    <div class="servings-box">33 Servings</div>
    <div class="weight-box">1000 gm.</div>
  </main>
</body>
</html>
```